Hydraulics Company Business Card Design

Modern business card design for a hydraulics company.
Our company colours are - black, orange and white.
I would like the following contact details included-
Name
Position
Phone number
Email
Website
Street Address

I have attached our company logo.
I would like the back of the card white.

Thank you.

```html
<!DOCTYPE html>
<html lang="en">
<head>
<meta charset="utf-8">
<title>Kestrel Ridge Hydraulics – Business Card</title>
<link rel="stylesheet" href="https://fonts.googleapis.com/css2?family=Montserrat:wght@500;700;800&family=Roboto:wght@400;500&display=swap">
<style>
  :root {
    --black: #050505;
    --orange: #f59c12;
    --white: #ffffff;
    --backdrop: #bdbdbd;
    --muted: #e9e9e9;
  }
  * { box-sizing: border-box; margin: 0; padding: 0; }
  html, body {
    width: 1200px; height: 802px; overflow: hidden;
    background: var(--backdrop);
  }
  .sheet {
    width: 1200px; height: 802px;
    display: flex; align-items: center; justify-content: center; gap: 40px;
  }
  .card {
    position: relative;
    width: 540px; height: 309px;
    border-radius: 22px;
    overflow: hidden;
    box-shadow: 0 10px 24px rgba(0,0,0,.25);
  }

  /* Front */
  .card--front { background: var(--black); color: var(--white); }
  .wordmark {
    position: absolute; left: 34px; top: 36px;
    font-family: "Montserrat", sans-serif; font-weight: 800;
    color: var(--orange); line-height: 1;
  }
  .wordmark__line1 { display: block; font-size: 40px; letter-spacing: -0.5px; }
  .wordmark__line2 { display: block; font-size: 22px; letter-spacing: 2px; margin-top: 6px; }

  .person {
    position: absolute; left: 60px; top: 176px; text-align: right; width: 180px;
    font-family: "Montserrat", sans-serif;
  }
  .person__name { font-size: 21px; font-weight: 700; color: var(--orange); }
  .person__role { font-size: 13px; font-weight: 500; color: var(--white); margin-top: 4px; }

  .divider {
    position: absolute; left: 262px; top: 158px; width: 1px; height: 74px;
    background: linear-gradient(to bottom, transparent, var(--orange), transparent);
  }

  .contacts {
    position: absolute; left: 282px; top: 150px; list-style: none;
    font-family: "Roboto", sans-serif; font-size: 14px; color: var(--white);
  }
  .contacts li { display: flex; align-items: center; gap: 10px; height: 28px; }
  .contacts svg { width: 15px; height: 15px; flex: none; }

  .address-band {
    position: absolute; left: 0; right: 0; bottom: 18px; height: 40px;
    background: var(--orange); color: var(--black);
    display: flex; align-items: center; justify-content: center; gap: 10px;
    font-family: "Roboto", sans-serif; font-size: 14px; font-weight: 500;
  }
  .address-band svg { width: 14px; height: 16px; }

  /* Back */
  .card--back {
    background: var(--white);
    display: flex; align-items: center; justify-content: center;
  }
  .card--back .wordmark {
    position: static; text-align: left;
  }
  .card--back .wordmark__line1 { font-size: 50px; }
  .card--back .wordmark__line2 { font-size: 28px; letter-spacing: 3px; }
</style>
</head>
<body>
<main class="sheet">
  <section class="card card--front" aria-label="Business card front">
    <div class="wordmark">
      <span class="wordmark__line1">Kestrel Ridge</span>
      <span class="wordmark__line2">HYDRAULICS</span>
    </div>

    <div class="person">
      <p class="person__name">Daniel Marsh</p>
      <p class="person__role">Owner</p>
    </div>

    <div class="divider"></div>

    <ul class="contacts">
      <li>
        <svg viewBox="0 0 16 16" aria-hidden="true"><circle cx="8" cy="8" r="8" fill="var(--orange)"/><path d="M5 4.5l1.6-.4.9 2-1 .8a5 5 0 0 0 2.6 2.6l.8-1 2 .9-.4 1.6c-3.5.3-6.8-3-6.5-6.5z" fill="var(--black)"/></svg>
        <span>123.456.7890</span>
      </li>
      <li>
        <svg viewBox="0 0 16 16" aria-hidden="true"><circle cx="8" cy="8" r="8" fill="var(--orange)"/><rect x="4" y="5" width="8" height="6" fill="var(--black)"/><path d="M4 5l4 3.2L12 5" stroke="var(--orange)" stroke-width="1" fill="none"/></svg>
        <span>info@webname.com</span>
      </li>
      <li>
        <svg viewBox="0 0 16 16" aria-hidden="true"><circle cx="8" cy="8" r="8" fill="var(--orange)"/><circle cx="8" cy="8" r="4.2" fill="none" stroke="var(--black)" stroke-width="1.2"/><path d="M3.8 8h8.4M8 3.8c-2 2.5-2 5.9 0 8.4M8 3.8c2 2.5 2 5.9 0 8.4" stroke="var(--black)" stroke-width="1" fill="none"/></svg>
        <span>www.website.com</span>
      </li>
    </ul>

    <div class="address-band">
      <svg viewBox="0 0 14 16" aria-hidden="true"><path d="M7 0a5.5 5.5 0 0 0-5.5 5.5C1.5 9.6 7 16 7 16s5.5-6.4 5.5-10.5A5.5 5.5 0 0 0 7 0z" fill="var(--black)"/><circle cx="7" cy="5.5" r="2" fill="var(--orange)"/></svg>
      <span>421, Address line goes here 45452, Country name</span>
    </div>
  </section>

  <section class="card card--back" aria-label="Business card back">
    <div class="wordmark">
      <span class="wordmark__line1">Kestrel Ridge</span>
      <span class="wordmark__line2">HYDRAULICS</span>
    </div>
  </section>
</main>
</body>
</html>
```